The Bayfield Wellness Clinic - Practice Flyer

We need a flyer that generally advertises our services. I've uploaded one old flyer as well as examples of others. I like the style of the materials made by this practice: https://www.facebook.com/PineRidgeCounselingHouse

```html
<!DOCTYPE html>
<html lang="en">
<head>
<meta charset="utf-8">
<title>The Bayfield Wellness Clinic – Practice Flyer</title>
<link rel="stylesheet" href="https://fonts.googleapis.com/css2?family=Merriweather:wght@300;400;700&display=swap">
<style>
  :root {
    --olive: #939862;
    --olive-deep: #7d9a3a;
    --ring: #7a9a34;
    --forest: #2e3f2c;
    --ink: #3b3a33;
    --paper: #f3f3ee;
    --mint: #e2ead0;
    --cord: #3d3529;
    --white: #ffffff;
    --serif: "Merriweather", Georgia, serif;
  }
  * { box-sizing: border-box; margin: 0; padding: 0; }
  html, body { width: 927px; height: 1200px; overflow: hidden; background: var(--paper); }
  .flyer {
    position: relative; width: 927px; height: 1200px; overflow: hidden;
    font-family: var(--serif); color: var(--ink);
    background: linear-gradient(180deg, var(--paper) 0%, var(--paper) 22%, var(--mint) 55%, #edf1e2 85%, var(--paper) 100%);
  }
  .abs { position: absolute; }
  .center { left: 0; width: 927px; text-align: center; }

  .masthead-band { top: 77px; left: 0; width: 927px; height: 51px; background: var(--olive); }
  .masthead-name { top: 80px; font-size: 33px; line-height: 44px; font-weight: 400; color: var(--white); letter-spacing: 0.5px; }
  .masthead-sub { top: 140px; font-size: 15px; line-height: 20px; font-weight: 700; color: var(--forest); letter-spacing: 0.5px; }

  .photos { top: 0; left: 0; }

  .intro { top: 527px; font-size: 19px; line-height: 26px; font-weight: 300; }
  .intro b { font-weight: 700; }

  .conditions {
    top: 620px; left: 30px; width: 867px; height: 162px; border-radius: 20px;
    background: var(--olive); color: var(--white); text-align: center; padding-top: 11px;
  }
  .conditions-lead { font-size: 17.5px; line-height: 23px; font-weight: 400; }
  .conditions-lead b { font-weight: 700; }
  .conditions-list { margin-top: 8px; font-size: 18px; line-height: 22.5px; font-weight: 700; }

  .method { top: 797px; font-size: 18.5px; line-height: 25px; font-weight: 300; }
  .method b { font-weight: 700; }

  .treatments {
    top: 882px; left: 31px; width: 864px; height: 127px; border: 1.5px solid var(--olive);
    border-radius: 20px; text-align: center; padding-top: 23px;
    font-size: 17px; line-height: 22.5px; font-weight: 700; color: var(--ink);
  }
  .treatments-label {
    top: 867px; left: 327px; width: 254px; height: 34px; border-radius: 12px;
    background: var(--olive-deep); color: var(--white); font-size: 19px; font-weight: 700;
    text-align: center; line-height: 34px;
  }

  .director { top: 1026px; font-size: 18px; line-height: 24.5px; font-weight: 400; }

  .footer-wave { top: 1050px; left: 0; }
  .brand-mark {
    top: 1057px; left: 19px; width: 124px; height: 124px; background: #3a3f35;
    color: var(--white); font-size: 32px; font-weight: 700; text-align: center; line-height: 124px;
  }
  .contact-phone { top: 1119px; font-size: 29px; line-height: 38px; font-weight: 700; color: var(--white); }
  .contact-rule { top: 1138px; height: 1.5px; background: var(--white); width: 81px; }
  .contact-web { top: 1157px; font-size: 25px; line-height: 32px; font-weight: 400; color: var(--white); }
  .social { top: 1129px; width: 40px; height: 40px; border-radius: 50%; background: #5f6a3f; }
</style>
</head>
<body>
<main class="flyer">

  <div class="abs masthead-band"></div>
  <div class="abs center masthead-name">The Bayfield Wellness Clinic</div>
  <div class="abs center masthead-sub">of GREATER BAYFIELD LLC</div>

  <svg class="abs photos" width="927" height="520" viewBox="0 0 927 520">
    <path d="M0 222 Q60 245 150 280 Q300 300 464 290 Q640 300 780 280 Q880 250 927 222" fill="none" stroke="var(--cord)" stroke-width="9"/>
    <g fill="none" stroke="#b4bd8e" stroke-width="1.2">
      <circle cx="154" cy="299" r="138"/>
      <circle cx="464" cy="349" r="164"/>
      <circle cx="774" cy="299" r="138"/>
    </g>
    <defs>
      <linearGradient id="tone-left" x1="0" y1="0" x2="1" y2="1"><stop offset="0" stop-color="#3a3530"/><stop offset="1" stop-color="#8aa6c0"/></linearGradient>
      <linearGradient id="tone-mid" x1="0" y1="0" x2="0" y2="1"><stop offset="0" stop-color="#b9b648"/><stop offset="1" stop-color="#c9b9a6"/></linearGradient>
      <linearGradient id="tone-right" x1="0" y1="0" x2="1" y2="1"><stop offset="0" stop-color="#c7dbe6"/><stop offset="1" stop-color="#7f7a74"/></linearGradient>
    </defs>
    <circle cx="154" cy="299" r="127" fill="url(#tone-left)" stroke="var(--ring)" stroke-width="5" role="img" aria-label="Photo: a man resting his head in his hand beside a rainy window"/>
    <circle cx="464" cy="349" r="152" fill="url(#tone-mid)" stroke="var(--ring)" stroke-width="5" role="img" aria-label="Photo: a happy family of four outdoors among autumn trees"/>
    <circle cx="774" cy="299" r="127" fill="url(#tone-right)" stroke="var(--ring)" stroke-width="5" role="img" aria-label="Photo: a woman leaning her head against a window, eyes closed"/>
  </svg>

  <p class="abs center intro">
    <b>The Bayfield Wellness Clinic</b> of Greater Bayfield, (BWC) provides expert<br>
    clinical care for <b>anxiety disorders, obsessive compulsive and related disorders,</b><br>
    and <b>neurodevelopmental disorders</b> in children, adolescents, and adults.
  </p>

  <section class="abs conditions">
    <p class="conditions-lead"><b>BWC</b> proudly provides the Greater Bayfield community with state-of-art<br>assessment and evidence-based therapist for disorders including:</p>
    <p class="conditions-list">
      Obsessive Compulsive Disorder • Trichotillomania • Excoriation Disorder<br>
      Generalized Anxiety Disorder • Panic Disorder • Specific Phobias • Hoarding Disorder<br>
      Body Dysmophic Disorder • Tic Disorder • ADHD Learning Disorders • Insomnia<br>
      Social Anxiety Disorder
    </p>
  </section>

  <p class="abs center method">
    <b>BWC</b> clinicians are highly trained in c<b>ognitive behavioral therapy (CBT),</b> which includes<br>
    scientifically informed techniques that are tailored to each client’s unique needs.
  </p>

  <section class="abs treatments">
    Cognitive Behavioral Therapy (CBT) • Exposure and Response Prevention (E/RP)<br>
    Comprehensive Behavioral (ComB)/Habit Reversal Training (HRT)<br>
    Cognitive Behavioral Intervention for Tics (CBIT) • Acceptance and Commitment Therapy (ACT)<br>
    Organizational Skills Training (OST) • CBT for Insomnia (CBT-I)
  </section>
  <div class="abs treatments-label">Treatments We Provide:</div>

  <p class="abs center director">
    Dana R. Whitmore, PsyD • Executive Director Licensed Psychologist<br>
    New Jersey Lic. No. 35S10000000 • Pennsylvania Lic. No. PS0000000
  </p>

  <svg class="abs footer-wave" width="927" height="150" viewBox="0 0 927 150" aria-hidden="true">
    <path d="M0 15 Q460 60 927 25 V150 H0 Z" fill="var(--white)"/>
    <path d="M0 40 Q460 80 927 45 V150 H0 Z" fill="var(--olive)"/>
  </svg>

  <div class="abs brand-mark">BWC</div>
  <div class="abs contact-rule" style="left:198px"></div>
  <div class="abs contact-rule" style="left:618px"></div>
  <div class="abs center contact-phone">Tel: (555) 014-3827</div>
  <div class="abs center contact-web">www.BayfieldWellnessClinic.com</div>
  <div class="abs social" style="left:766px" aria-label="Social link"></div>
  <div class="abs social" style="left:817px" aria-label="Social link"></div>
  <div class="abs social" style="left:868px" aria-label="Social link"></div>

</main>
</body>
</html>
```